Business Card for staff member of football club SC Brenval

I would like to get a business card template for all staff member of our soccer club.

The card should use as much as possible the 2 colors of the club : Red which is the main color and blue which is the alternative color. It can be balanced between the two like our logo.

I prefer simple and lean design.

Contact Information for Business Card

Bussiness card should have all main stuff as describe here below in must have.

Font styles to use
Sans Serif

Requirements
Must have
• Name : Laurent DESPRATIN
Fonction : Président
Mobile : +41 xx xxx xx xx
Email : first.lastname@scbrenval.ch
Adresse of the club : SC Brenval, 1873 Brenval
Website of the club : www.scbrenval.ch
Nice to have
• Version with and without picture of the staff member

A version for men, a version for women staff member.

```html
<!DOCTYPE html>
<html lang="fr">
<head>
<meta charset="utf-8">
<title>SC Brenval – Carte de visite</title>
<link rel="stylesheet" href="https://fonts.googleapis.com/css2?family=Oswald:wght@500;600&family=Work+Sans:wght@400&display=swap">
<style>
  :root {
    --club-red: #e8213a;
    --club-blue: #0a88cc;
    --ink: #231f20;
    --paper: #ffffff;
    --backdrop: #4a3324;
    --ball-tone: #3a3536;
  }
  * { margin: 0; padding: 0; box-sizing: border-box; }
  html, body { width: 1200px; height: 900px; overflow: hidden; }
  body { background: var(--backdrop); position: relative; }

  .card {
    position: absolute;
    width: 347px;
    height: 605px;
    top: 148px;
  }
  .card--front { left: 218px; }
  .card--back { left: 637px; }
  .card__shape { position: absolute; inset: 0; width: 100%; height: 100%; }

  .club-name {
    position: absolute;
    left: 0; right: 0;
    text-align: center;
    font-family: "Oswald", sans-serif;
    font-weight: 600;
    font-size: 54px;
    line-height: 1;
    letter-spacing: 0.5px;
  }
  .card--front .club-name { top: 58px; color: var(--club-red); }
  .card--back .club-name { top: 262px; color: var(--paper); }

  .ball {
    position: absolute;
    left: 102px; top: 148px;
    width: 142px; height: 142px;
    border-radius: 50%;
    background: radial-gradient(circle at 50% 45%, #6a6465 0%, var(--ball-tone) 70%, var(--ink) 100%);
  }

  .staff-name {
    position: absolute;
    top: 316px; left: 0; right: 0;
    text-align: center;
    font-family: "Oswald", sans-serif;
    font-weight: 500;
    font-size: 25px;
    line-height: 1;
    letter-spacing: 0.5px;
  }
  .staff-name__first { color: var(--club-red); }
  .staff-name__last { color: var(--club-blue); }

  .staff-role {
    position: absolute;
    top: 346px; left: 0; right: 0;
    text-align: center;
    font-family: "Work Sans", sans-serif;
    font-size: 17px;
    color: var(--ink);
    letter-spacing: 0.3px;
  }

  .contact-icons {
    position: absolute;
    top: 380px; left: 0; right: 0;
    display: flex;
    justify-content: center;
    gap: 10px;
  }
  .contact-icons svg { width: 13px; height: 13px; }

  .contact-list {
    position: absolute;
    top: 405px; left: 0; right: 0;
    list-style: none;
    text-align: center;
    font-family: "Work Sans", sans-serif;
    font-size: 15px;
    line-height: 20.5px;
    color: var(--ink);
    letter-spacing: 0.3px;
  }
</style>
</head>
<body>

  <section class="card card--front">
    <svg class="card__shape" viewBox="0 0 578 1008" aria-hidden="true">
      <polygon points="0,0 578,0 578,795 289,1008 0,795" fill="var(--paper)"/>
      <polyline points="274,23 23,23 23,780 274,965" fill="none" stroke="var(--club-red)" stroke-width="12"/>
      <polyline points="304,23 555,23 555,780 304,965" fill="none" stroke="var(--club-blue)" stroke-width="12"/>
    </svg>

    <div class="club-name">SC BRENVAL</div>
    <div class="ball" role="img" aria-label="Illustration d'un ballon de football"></div>

    <div class="staff-name"><span class="staff-name__first">LAURENT</span> <span class="staff-name__last">DESPRATIN</span></div>
    <div class="staff-role">Président</div>

    <div class="contact-icons">
      <svg viewBox="0 0 16 16" aria-label="Téléphone"><path d="M4 1.5 L6 4.5 L4.8 6 C5.6 8 7.5 10.2 9.8 11.2 L11.3 10 L14.5 12 L13 14.5 C8 14.5 2 8.5 1.8 3.5 Z" fill="none" stroke="var(--club-red)" stroke-width="1.4" stroke-linejoin="round"/></svg>
      <svg viewBox="0 0 16 16" aria-label="E-mail"><rect x="1.5" y="3.5" width="13" height="9" fill="none" stroke="var(--club-red)" stroke-width="1.4"/><polyline points="1.5,3.5 8,9 14.5,3.5" fill="none" stroke="var(--club-red)" stroke-width="1.4"/></svg>
      <svg viewBox="0 0 16 16" aria-label="Site web"><circle cx="8" cy="8" r="6.5" fill="none" stroke="var(--club-red)" stroke-width="1.2"/><ellipse cx="8" cy="8" rx="2.8" ry="6.5" fill="none" stroke="var(--club-red)" stroke-width="1.1"/><line x1="1.5" y1="8" x2="14.5" y2="8" stroke="var(--club-red)" stroke-width="1.1"/><line x1="2.5" y1="5" x2="13.5" y2="5" stroke="var(--club-red)" stroke-width="1"/><line x1="2.5" y1="11" x2="13.5" y2="11" stroke="var(--club-red)" stroke-width="1"/></svg>
      <svg viewBox="0 0 16 16" aria-label="Adresse"><path d="M8 15 C5 10.5 3 8.3 3 6 A5 5 0 0 1 13 6 C13 8.3 11 10.5 8 15 Z" fill="var(--club-red)"/><circle cx="8" cy="6" r="1.8" fill="var(--paper)"/></svg>
    </div>

    <ul class="contact-list">
      <li>+41 xx xxx xx xx</li>
      <li>first.lastname@scbrenval.ch</li>
      <li>www.scbrenval.ch</li>
      <li>SC Brenval, 1873 Brenval</li>
    </ul>
  </section>

  <section class="card card--back">
    <svg class="card__shape" viewBox="0 0 578 1008" aria-hidden="true">
      <polygon points="0,0 578,0 578,795 289,1008 0,795" fill="var(--ink)"/>
      <polyline points="274,23 21,23 21,780 274,965" fill="none" stroke="var(--club-red)" stroke-width="12"/>
      <polyline points="304,23 557,23 557,780 304,965" fill="none" stroke="var(--club-blue)" stroke-width="12"/>
    </svg>
    <div class="club-name">SC BRENVAL</div>
  </section>

</body>
</html>
```